Banner für Immobilienmakler
Zielgruppe
Immobilienmakler, Immobilienverkauf mit Herz,
Aufgabenstellung
Verkauf von Häusern und Wohnungen, der Banner soll an einen Balkon oder einen Zaun angebracht werden mit dem Hinweis, dass das Haus Zu verkaufen ist.
Maße ca. 76 x 244cm
Es darf gerne frech und modern sein mit einem witzigen einladenden Spruch sein, sollte aber auch ansonsten zu meinem chicen Style passen (siehe Homepage www.kranichhausverkauf.de) es soll sich abheben von anderen langweiligen Bannern.
Ggf soll die Plane auch noch an einem Tennisplatz angebracht werden

```html
<!DOCTYPE html>
<html lang="de">
<head>
<meta charset="utf-8">
<title>Banner – Kranich Immobilien</title>
<link href="https://fonts.googleapis.com/css2?family=Open+Sans:wght@400;600;800&display=swap" rel="stylesheet">
<style>
  :root {
    --page: #ebebeb;
    --banner: #1c1c1c;
    --white: #ffffff;
    --gold: #c4ae87;
    --paper-light: #ffffff;
    --paper-shade: #e9e9ec;
    --ink: #1c1c1c;
  }
  * { margin: 0; padding: 0; box-sizing: border-box; }
  html, body {
    width: 1200px; height: 576px; overflow: hidden;
    background: var(--page);
    font-family: "Open Sans", Arial, sans-serif;
  }
  .banner {
    position: absolute; left: 100px; top: 132px;
    width: 1000px; height: 312px;
    background: var(--banner);
    box-shadow: 0 0 28px rgba(0,0,0,0.08);
    overflow: hidden;
  }
  .banner__corner { position: absolute; inset: 0; }
  .headline {
    position: absolute; left: 54px; top: 42px;
    font-weight: 800; line-height: 1; white-space: nowrap;
  }
  .headline__lead {
    display: block; color: var(--white);
    font-size: 47px; letter-spacing: -0.4px;
  }
  .headline__punch {
    display: block; color: var(--gold);
    font-size: 58px; margin-top: 15px; letter-spacing: -0.1px;
  }
  .contacts {
    position: absolute; left: 57px; top: 251px;
    display: flex; gap: 46px;
  }
  .contact {
    display: flex; align-items: center; gap: 10px;
    color: var(--white); font-size: 31px; font-weight: 400; line-height: 1;
    white-space: nowrap;
  }
  .contact__icon { width: 25px; height: 25px; flex: none; }
  .brand {
    position: absolute; right: 16px; top: 262px;
    display: flex; align-items: center; gap: 8px;
    color: var(--ink); font-size: 13px; font-weight: 600;
    letter-spacing: 0.8px; white-space: nowrap; line-height: 1;
  }
  .brand__dot {
    width: 10px; height: 10px; border-radius: 50%;
    background: var(--gold); flex: none;
  }
</style>
</head>
<body>
  <section class="banner">
    <svg class="banner__corner" viewBox="0 0 1000 312" width="1000" height="312">
      <defs>
        <linearGradient id="paper" x1="0" y1="1" x2="1" y2="0">
          <stop offset="0" stop-color="var(--paper-light)"/>
          <stop offset="1" stop-color="var(--paper-shade)"/>
        </linearGradient>
      </defs>
      <path d="M1000,86 C940,215 800,285 642,312 L1000,312 Z" fill="url(#paper)"/>
      <path d="M1000,86 C940,215 800,285 642,312" fill="none" stroke="var(--gold)" stroke-width="4"/>
    </svg>

    <h1 class="headline">
      <span class="headline__lead">KAUFEN SIE DIESES HAUS NICHT</span>
      <span class="headline__punch">- ES IST ZU PERFEKT FÜR SIE</span>
    </h1>

    <div class="contacts">
      <div class="contact">
        <svg class="contact__icon" viewBox="0 0 24 24">
          <path d="M5 3 L8.5 2.5 L10 7 L8 8.8 C9 11.5 11 13.8 13.5 15.2 L15.3 13.2 L19.8 14.8 L19.3 18.3 C19 19.5 17.8 20.3 16.5 20 C10 18.6 4.9 13.5 3.6 7 C3.4 5 4 3.5 5 3 Z" fill="var(--gold)"/>
          <path d="M13 2.5 A8.5 8.5 0 0 1 21.5 11 M13 5.5 A5.5 5.5 0 0 1 18.5 11 M13 8.3 A2.7 2.7 0 0 1 15.7 11" fill="none" stroke="var(--gold)" stroke-width="1.1"/>
        </svg>
        <span>0176 - 4829031</span>
      </div>
      <div class="contact">
        <svg class="contact__icon" viewBox="0 0 24 24">
          <path d="M5 3 L8.5 2.5 L10 7 L8 8.8 C9 11.5 11 13.8 13.5 15.2 L15.3 13.2 L19.8 14.8 L19.3 18.3 C19 19.5 17.8 20.3 16.5 20 C10 18.6 4.9 13.5 3.6 7 C3.4 5 4 3.5 5 3 Z" fill="var(--gold)"/>
          <path d="M13 2.5 A8.5 8.5 0 0 1 21.5 11 M13 5.5 A5.5 5.5 0 0 1 18.5 11 M13 8.3 A2.7 2.7 0 0 1 15.7 11" fill="none" stroke="var(--gold)" stroke-width="1.1"/>
        </svg>
        <span>02241 – 70 60 418</span>
      </div>
    </div>

    <div class="brand">
      <span class="brand__dot"></span>
      <span class="brand__name">KRANICH IMMOBILIEN</span>
    </div>
  </section>
</body>
</html>
```